LOCKVIA WEBSEITE (HAAR/FRISEUR/PERÜCKEN)
Aufgabenstellung
Was genau soll gestaltet werden?
-Webdesign
-eine Startseite mit einem Produktfenster und sechs Designs für das Fenster mit dem jeweiligen Produkt (Slideshow für sechs unserer Produkte) siehe Erklärung
- 3 Unterseiten für Folgende Kategorien:
1. Haare ersetzten (Damit verdien wir unser Brot) oft wird hier in Frauen und Männer untergliedert (siehe Mitbewerber morbeck.de)
2. Produktübersicht!!!!! (wir haben etwa 10 wichtige Produkte, schnell, Intuitiv und Übersichtlich)
3. Velutrin Produktseite (mit Video Fenster)
Projektname
www.lockvia.de
Produktgruppe
Kosmetischer Haaresatz und Dienstleistungen von professionellen Lockvia Zweithaarstudios.
Content und Menübeispeil & Bilder:
Auf der folgenden Domain findet Ihr eine Muster Webseite mit der Groben Inhaltlichen Gestaltung: Text, Daten und Bilder Können verwendet werden.
wendlocke-pasing.schopfwerk.com
Bilder:
Siehe menüpunkt bilder für designer unter: wendlocke-pasing.schopfwerk.com
Mit Bildern sieht es etwas rar aus gerne können Bilder von euch eigebunden werden, welche wir noch erwerben müssen. Bildkram etc. (Budget: 50€)
Es können alle Bilder von folgenden Webseiten verwendet werden:
 1. wendlocke-pasing.schopfwerk.com 
http://www.lockvia.fr/
velutrin:
http://www.velutrin.co.uk/
http://www.velutrin-france.com/solution-cheveux/velutrin-france.asp
http://vidplex.example/kq7Rm2Zt9Pa
männer:
http://www.lockvia.fr/perruque-lockvia/cutiplan.asp
www.wurzelbond.de
laser:
http://www.lockvia.com/eng/pp-peigne.htm
http://www.tresslumo.com/
http://www.ratgeber-kopfpflege.com/Laser-Therapie_Haarausfall.html
http://haartransplantation.ratgeber-kopfpflege.com/laser_therapie.html
qorvo:
http://vidplex.example/Lw3Hs8Nd4Xe
Haartransplantation:
http://haartransplantation.ratgeber-kopfpflege.com/index.html
Zielgruppe
Unsere Zielgruppe sind Personen ..

```html
<!DOCTYPE html>
<html lang="de">
<head>
<meta charset="utf-8">
<title>Lockvia – Produkte</title>
<link href="https://fonts.googleapis.com/css2?family=Noto+Sans:wght@400;700&display=swap" rel="stylesheet">
<style>
:root{
  --brand-blue:#1a6fb4;
  --nav-dark:#5b5966;
  --text:#555560;
  --text-dark:#4a4a55;
  --frame:#6d6d75;
  --bg:#ffffff;
  --thumb-bg:#f4f4ee;
}
*{box-sizing:border-box;margin:0;padding:0}
html,body{width:1200px;height:581px;overflow:hidden;background:var(--bg)}
body{position:relative;font-family:"Noto Sans",sans-serif;color:var(--text)}
.abs{position:absolute}
.brand{left:163px;top:16px;font-size:30px;font-weight:700;color:var(--text-dark);line-height:36px}
.top-nav{left:473px;top:18px;display:flex;gap:8px;font-size:10.5px;white-space:nowrap}
.search{left:833px;top:16px;display:flex;align-items:center;font-size:10.5px}
.search-field{margin-left:6px;width:109px;height:16px;border:1px solid #888}
.search-btn{margin-left:6px;width:16px;height:16px;background:var(--nav-dark);color:#fff;font-size:8px;text-align:center;line-height:16px}
.rule{left:148px;width:910px;height:2px;background:var(--brand-blue)}
.flags{left:951px;top:61px;display:flex;gap:11px}
.main-nav{left:148px;top:87px;width:910px;height:27px;background:var(--nav-dark);display:flex;align-items:center;gap:20px;padding-left:11px;font-size:10.5px;color:#fff;white-space:nowrap}
.thumb-panel{left:148px;top:124px;width:201px;height:330px;border:1px solid var(--frame)}
.thumb{width:53px;height:53px;background:var(--thumb-bg)}
.product-shot{left:382px;top:169px;width:123px;height:120px;background:linear-gradient(90deg,#fbfbf7,#eef0d8 45%,#dce9ee 55%,#fbfbf7)}
.product-title{left:524px;top:142px;font-size:23px;font-weight:700;color:var(--text-dark)}
.product-copy{left:524px;top:186px;width:495px;font-size:11.5px;line-height:15px}
.side-box{left:1063px;width:108px;height:206px;border:1px solid var(--frame);padding:10px 3px 10px 9px;font-size:11px;line-height:15px}
.side-link{position:absolute;left:9px;bottom:30px;font-size:10px;display:flex;align-items:center;gap:5px;white-space:nowrap}
.footer-links{left:175px;top:523px;font-size:11px}
.footer-phone{left:356px;top:523px;font-size:11px}
.footer-copy{left:920px;top:521px;font-size:8px}
</style>
</head>
<body>
<div class="abs brand">LOCKVIA</div>
<nav class="abs top-nav"><span>Home</span><span>Kontakt</span><span>Spezialisten in Ihrer Nähe</span><span>Presse</span><span>News</span><span>Videos</span></nav>
<div class="abs search">Suche:<span class="search-field"></span><span class="search-btn">los</span></div>
<div class="abs rule" style="top:54px"></div>
<div class="abs flags">
  <svg width="14" height="10"><rect width="14" height="3.4" fill="#222"/><rect y="3.3" width="14" height="3.4" fill="#d21"/><rect y="6.6" width="14" height="3.4" fill="#fc0"/></svg>
  <svg width="14" height="10"><rect width="14" height="10" fill="#c33"/><rect y="1.5" width="14" height="1.4" fill="#fff"/><rect y="4.3" width="14" height="1.4" fill="#fff"/><rect y="7.1" width="14" height="1.4" fill="#fff"/><rect width="6" height="5.5" fill="#336"/></svg>
  <svg width="14" height="10"><rect width="4.7" height="10" fill="#24a"/><rect x="4.7" width="4.7" height="10" fill="#fff" stroke="#ddd" stroke-width=".5"/><rect x="9.4" width="4.6" height="10" fill="#d22"/></svg>
</div>
<div class="abs rule" style="top:85px"></div>
<nav class="abs main-nav"><span>Home</span><span>Produktgruppen</span><span>Haarlösungen</span><span>Philosophie Haarausfall</span><span>Login</span></nav>

<aside class="abs thumb-panel">
  <div class="abs thumb" style="left:27px;top:11px" role="img" aria-label="Produktfoto Flasche"></div>
  <div class="abs thumb" style="left:119px;top:11px" role="img" aria-label="Produktfoto Sprühflasche"></div>
  <div class="abs thumb" style="left:27px;top:70px" role="img" aria-label="Produktfoto Sprühflasche grün"></div>
  <div class="abs thumb" style="left:119px;top:70px" role="img" aria-label="Produktfoto Sprühflasche grün"></div>
  <div class="abs thumb" style="left:27px;top:127px" role="img" aria-label="Produktfoto Flasche gelb"></div>
  <div class="abs thumb" style="left:119px;top:127px" role="img" aria-label="Produktfoto Sprühflasche"></div>
  <div class="abs thumb" style="left:27px;top:184px" role="img" aria-label="Produktfoto Spray"></div>
  <div class="abs thumb" style="left:119px;top:184px" role="img" aria-label="Produktfoto Sprühflasche grün"></div>
  <div class="abs thumb" style="left:27px;top:242px" role="img" aria-label="Produktfoto Tube"></div>
</aside>

<div class="abs product-shot" role="img" aria-label="Produktfoto Shampooflasche"></div>
<h1 class="abs product-title">Produkname 1</h1>
<p class="abs product-copy">Lorem ipsum dolor sit amet, consetetur sadipscing elitr, sed diam nonumy eirmod tempor invidunt ut labore et dolore magna aliquyam erat, sed diam voluptua. At vero eos et accusam et justo duo dolores et ea rebum. Stet clita kasd gubergren, no sea takimata sanctus est Lorem ipsum dolor sit amet. Lorem ipsum dolor sit amet, consetetur sadipscing elitr, sed diam nonumy eirmod tempor invidunt ut labore et dolore magna aliquyam erat, sed diam voluptua. At vero eos et accusam et justo duo dolores et ea rebum. Stet clita kasd gubergren, no sea takimata sanctus est Lorem ipsum dolor sit amet.</p>

<aside class="abs side-box" style="top:85px">Bestellen Sie jetzt kostenfrei die Lockvia Broschüre mit den 10 Besten Tips wie Sie Ihren Haarausfall stoppen.
  <span class="side-link"><svg width="7" height="7"><path d="M0 0L7 3.5L0 7Z" fill="#444"/></svg>Hier bestellen</span></aside>
<aside class="abs side-box" style="top:309px">Sie leiden unter Haarausfall analysieren Sie hier wie stark sich der Haarausfall entwickeln wird.
  <span class="side-link"><svg width="7" height="7"><path d="M0 0L7 3.5L0 7Z" fill="#444"/></svg>Hier analysieren</span></aside>

<div class="abs rule" style="top:514px"></div>
<footer>
  <div class="abs footer-links">Kontakt &nbsp;|&nbsp; AGB &nbsp;|&nbsp; Impressum</div>
  <div class="abs footer-phone">Telefon: 0049 (0) 761/4827715-204</div>
  <div class="abs footer-copy">www.lockvia.de © 2011</div>
</footer>
</body>
</html>
```